Bright Harbor Property Institute

This must be done in word press and I will need about 7 tabs The home page, Information page, Schedule and Cost page which will link to a Email me form, a online registration a about us and location/contact tab Each tab will then open several other pages. The home page will describe different courses that we offer since all the schools are about the same you can get a good ideal by going to plomvex.example or keelwardhomeclasses.example and looking at their site I would like mine to be similar as the courses are exactly the same but I would like the site to be more modern I also need it to be in word press so I can change it and update the dates as they change I have attached he logo below

Target Market(s)

people interested in getting into real estate and those who need continuing education

Coding

Number of Pages Required

Font styles to use
Sans Serif

Colors
3276b5

Requirements
Must have
• A page to schedule classes, a tab so the college I am partnering with can link the online courses to the back side, a page that describes the type of classes I offer

```html
<!DOCTYPE html>
<html lang="en">
<head>
<meta charset="utf-8">
<title>Bright Harbor Property Institute</title>
<link href="https://fonts.googleapis.com/css2?family=Roboto:wght@400;500;700&family=Open+Sans:wght@400;600&display=swap" rel="stylesheet">
<style>
:root{
  --blue:#2c5fa8;
  --ink:#1c1c1c;
  --muted:#7a7a7a;
  --header-bg:#fcf2f2;
  --graphite:#454648;
  --card:#eeeef2;
  --line:#d9d9d9;
  --white:#ffffff;
}
*{box-sizing:border-box;margin:0;padding:0}
html,body{width:1200px;height:3735px;overflow:hidden}
body{position:relative;font-family:"Open Sans",sans-serif;color:var(--ink);background:var(--white)}
.abs{position:absolute}
.centered{display:inline-flex;align-items:center;justify-content:center}

.site-header{left:0;top:0;width:1200px;height:160px;background:var(--header-bg)}
.icon-ring{width:44px;height:44px;border:1.5px solid var(--blue);border-radius:50%;display:flex;align-items:center;justify-content:center}
.call-label{left:166px;top:20px;font:500 15px "Roboto",sans-serif}
.call-number{left:166px;top:38px;font:700 20px "Roboto",sans-serif;letter-spacing:.5px}
.brand{left:440px;top:26px;width:320px;text-align:center;white-space:nowrap}
.brand-name{font:700 28px/30px "Roboto",sans-serif;color:var(--blue);letter-spacing:1px}
.brand-sub{font:400 12px "Roboto",sans-serif;color:var(--blue);letter-spacing:1px}
.email{left:886px;top:34px;font:400 15px "Open Sans",sans-serif;white-space:nowrap}
.main-nav{left:110px;top:120px;width:980px;display:flex;justify-content:space-between;font:500 15px "Roboto",sans-serif}
.main-nav .active{color:var(--blue)}

.hero{left:0;top:160px;width:1200px;height:560px;background:linear-gradient(100deg,#6c7a5a 0%,#a9a575 35%,#8d8a5c 60%,#5b5f3e 100%)}
.hero-box{left:545px;top:348px;width:545px;height:184px;background:rgba(50,50,50,.78);text-align:center;color:var(--white)}
.hero-box h1{margin-top:20px;font:700 25px/34px "Roboto",sans-serif;white-space:nowrap}
.hero-box p{margin-top:6px;font:400 15px/26px "Open Sans",sans-serif;padding:0 50px}
.pill{background:var(--blue);color:var(--white);font:500 15px "Roboto",sans-serif;border-radius:22px;width:172px;height:40px;margin-top:10px}
.dots{left:570px;top:684px;display:flex;gap:6px}
.dots span{width:10px;height:10px;border-radius:50%;border:1px solid var(--white)}
.dots .on{background:var(--blue);border-color:var(--blue)}

.section-title{left:0;width:1200px;text-align:center;font:500 30px "Roboto",sans-serif}
.divider{left:455px;width:290px;height:48px}

.feature{width:320px;text-align:center}
.feature h3{font:500 20px "Roboto",sans-serif;margin-top:30px}
.feature p{font:400 15px/26px "Open Sans",sans-serif;color:var(--muted);margin-top:12px}
.feature-icon{width:116px;height:116px;margin:0 auto;border-radius:50%;background:var(--white);box-shadow:0 2px 8px rgba(0,0,0,.18);display:flex;align-items:center;justify-content:center}
.feature-icon.filled{background:var(--blue);box-shadow:0 0 0 10px var(--white),0 0 0 13px rgba(44,95,168,.5)}
.btn-outline{margin-top:18px;width:160px;height:46px;border:2px solid var(--blue);border-radius:23px;font:500 15px "Roboto",sans-serif;color:var(--ink)}
.btn-solid{background:var(--blue);color:var(--white)}

.course{height:441px}
.course-text{color:var(--white)}
.course-text h4{font:500 15px "Roboto",sans-serif;text-transform:uppercase}
.course-text .price{font:500 26px "Roboto",sans-serif;margin-top:20px}
.course-list{display:grid;grid-template-columns:180px 180px;row-gap:12px;margin-top:12px;font:400 16px "Open Sans",sans-serif}
.course-list li{list-style:none}
.book{margin-top:24px;width:158px;height:50px;border:2px solid var(--white);font:500 15px "Roboto",sans-serif}

.about-card{left:110px;top:2670px;width:978px;height:373px;background:var(--card);box-shadow:0 2px 8px rgba(0,0,0,.15)}
.about-card h3{position:absolute;left:25px;top:36px;font:500 20px "Roboto",sans-serif}
.about-card p{position:absolute;left:25px;top:68px;width:467px;font:400 15px/26px "Open Sans",sans-serif;color:var(--muted);text-align:justify}
.about-btn{position:absolute;left:25px;top:300px;width:131px;height:45px;background:var(--blue);color:var(--white);font:500 15px "Roboto",sans-serif}
.about-photo{left:620px;top:2692px;width:448px;height:378px;border:4px solid var(--white);box-shadow:0 2px 6px rgba(0,0,0,.2);background:linear-gradient(135deg,#3a2418 0%,#7a4a2a 45%,#a8682f 70%,#2a1b12 100%)}

.contact{left:0;top:3172px;width:1200px;height:465px;background:linear-gradient(90deg,#f2f2f2,#ececec)}
.contact h2{position:absolute;left:115px;top:36px;font:500 32px "Roboto",sans-serif}
.field{background:var(--white);border:1px solid #cfcfcf;font:400 13px "Open Sans",sans-serif;padding:12px 8px}
.submit{left:112px;top:3543px;width:471px;height:50px;background:var(--blue);color:var(--white);font:500 19px "Roboto",sans-serif}
.map{left:620px;top:3255px;width:465px;height:338px;background:linear-gradient(135deg,#e6e4df,#d9e4ec);border:1px solid #ddd}

.site-footer{left:0;top:3637px;width:1200px;height:98px;background:var(--blue)}
.social{left:113px;top:34px;display:flex;gap:10px}
.social span{width:32px;height:32px;border:2px solid var(--white);border-radius:50%}
.copyright{right:113px;top:40px;color:var(--white);font:400 15px "Open Sans",sans-serif}
</style>
</head>
<body>

<header class="site-header abs">
  <div class="icon-ring abs" style="left:110px;top:22px">
    <svg width="20" height="20" viewBox="0 0 24 24" fill="none" stroke="#2c5fa8" stroke-width="1.6"><path d="M5 3h4l2 5-2.5 1.5a11 11 0 0 0 6 6L16 13l5 2v4a2 2 0 0 1-2 2A16 16 0 0 1 3 5a2 2 0 0 1 2-2z"/></svg>
  </div>
  <div class="call-label abs">CALL NOW</div>
  <div class="call-number abs">555-010-4400</div>
  <div class="brand abs">
    <div class="brand-name">BRIGHT HARBOR</div>
    <div class="brand-sub">PROPERTY INSTITUTE</div>
  </div>
  <div class="icon-ring abs" style="left:828px;top:22px">
    <svg width="20" height="16" viewBox="0 0 24 18" fill="none" stroke="#2c5fa8" stroke-width="1.6"><rect x="1" y="1" width="22" height="16"/><path d="M1 1l11 9 11-9"/></svg>
  </div>
  <div class="email abs">info@bhpi.example</div>
  <svg class="abs" style="left:1030px;top:34px" width="24" height="20" viewBox="0 0 24 20" fill="none" stroke="#222" stroke-width="1.6"><path d="M1 2h4l3 11h12l2-8H7"/><circle cx="10" cy="17" r="1.5"/><circle cx="18" cy="17" r="1.5"/></svg>
  <svg class="abs" style="left:1074px;top:37px" width="14" height="14" viewBox="0 0 14 14" fill="none" stroke="#222" stroke-width="2"><circle cx="6" cy="6" r="4.5"/><path d="M9.5 9.5L13 13"/></svg>
  <nav class="main-nav abs">
    <span class="active">HOME</span><span>INFORMATION</span><span>SCHEDULE AND COST</span><span>REGISTRATION</span><span>ONLINE COURSES</span><span>ABOUT US</span><span>CONTACT</span>
  </nav>
</header>

<section class="hero abs" role="img" aria-label="Photo of a smiling student working on a laptop outdoors"></section>
<div class="hero-box abs">
  <h1>BRIGHT HARBOR PROPERTY INSTITUTE.</h1>
  <p>Nemo enim ipsam voluptatem quia voluptas sit aspernatur aut odit aut fugit, sed quia consequuntur</p>
  <span class="pill centered">GET STARTED</span>
</div>
<div class="dots abs"><span></span><span class="on"></span><span></span></div>

<h2 class="section-title abs" style="top:812px">WELCOME TO BRIGHT HARBOR PROPERTY INSTITUTE</h2>
<svg class="divider abs" style="top:864px" viewBox="0 0 290 48"><line x1="0" y1="24" x2="110" y2="24" stroke="#d9d9d9"/><line x1="180" y1="24" x2="290" y2="24" stroke="#d9d9d9"/><circle cx="145" cy="24" r="22" fill="#fff" stroke="#d9d9d9"/><circle cx="145" cy="24" r="8" fill="#2c5fa8"/></svg>

<div class="feature abs" style="left:111px;top:972px">
  <div class="feature-icon"><svg width="60" height="60" viewBox="0 0 60 60" fill="none" stroke="#2c5fa8" stroke-width="2"><circle cx="22" cy="18" r="8"/><path d="M8 40a14 14 0 0 1 28 0"/><rect x="16" y="38" width="36" height="16"/><circle cx="42" cy="26" r="6"/></svg></div>
  <h3>INFORMATION</h3>
  <p>Nemo enim ipsam voluptatem quia voluptas sit aspernatur aut odit aut fugit, sed quia consequuntur magni dolores eos qui ratione voluptatem</p>
  <span class="btn-outline centered">READ MORE</span>
</div>
<div class="feature abs" style="left:443px;top:972px">
  <div class="feature-icon filled"><svg width="60" height="60" viewBox="0 0 60 60" fill="none" stroke="#fff" stroke-width="2"><circle cx="24" cy="34" r="14"/><path d="M24 26v16M28 29h-6a3 3 0 0 0 0 6h4a3 3 0 0 1 0 6h-6"/><rect x="36" y="26" width="16" height="20"/></svg></div>
  <h3>SCHEDULE &amp; COST</h3>
  <p>Nemo enim ipsam voluptatem quia voluptas sit aspernatur aut odit aut fugit, sed quia consequuntur magni dolores eos qui ratione voluptatem</p>
  <span class="btn-outline btn-solid centered">READ MORE</span>
</div>
<div class="feature abs" style="left:774px;top:972px">
  <div class="feature-icon"><svg width="60" height="60" viewBox="0 0 60 60" fill="none" stroke="#2c5fa8" stroke-width="2.5"><path d="M34 12H14a4 4 0 0 0-4 4v30a4 4 0 0 0 4 4h30a4 4 0 0 0 4-4V28"/><path d="M44 8l8 8-20 20h-8v-8z"/></svg></div>
  <h3>REGISTRATION</h3>
  <p>Nemo enim ipsam voluptatem quia voluptas sit aspernatur aut odit aut fugit, sed quia consequuntur magni dolores eos qui ratione voluptatem</p>
  <span class="btn-outline centered">READ MORE</span>
</div>

<h2 class="section-title abs" style="top:1418px">BRIGHT HARBOR ONLINE COURSES</h2>
<svg class="divider abs" style="top:1470px" viewBox="0 0 290 48"><line x1="0" y1="24" x2="110" y2="24" stroke="#d9d9d9"/><line x1="180" y1="24" x2="290" y2="24" stroke="#d9d9d9"/><circle cx="145" cy="24" r="22" fill="#fff" stroke="#d9d9d9"/><circle cx="145" cy="24" r="8" fill="#2c5fa8"/></svg>

<section class="course abs" style="left:0;top:1559px;width:579px;background:var(--blue)">
  <div class="course-text abs" style="left:110px;top:98px">
    <h4>The Bright Harbor Property Principles Course</h4>
    <div class="price">$360.00</div>
    <ul class="course-list">
      <li>○ Lorem ipsum dolor</li><li>○ Nemo enim ipsam</li>
      <li>○ Nemo enim ipsam</li><li>○ Lorem ipsum dolor</li>
      <li>○ Lorem ipsum dolor</li><li>○ Nemo enim ipsam</li>
    </ul>
    <span class="book centered">BOOK NOW</span>
  </div>
</section>
<div class="course abs" role="img" aria-label="Photo of three students studying together with a laptop and books" style="left:579px;top:1559px;width:621px;background:linear-gradient(120deg,#9c8f52,#c9b99a 50%,#6a6450)"></div>

<div class="course abs" role="img" aria-label="Photo of a student working on a laptop in a cafe" style="left:0;top:2000px;width:578px;background:linear-gradient(110deg,#3d4a3a,#8a7d6c 55%,#6b3a34)"></div>
<section class="course abs" style="left:578px;top:2000px;width:622px;background:var(--graphite)">
  <div class="course-text abs" style="left:82px;top:98px">
    <h4>The Bright Harbor New Affiliates Course</h4>
    <div class="price">$165.00</div>
    <ul class="course-list">
      <li>○ Lorem ipsum dolor</li><li>○ Nemo enim ipsam</li>
      <li>○ Nemo enim ipsam</li><li>○ Lorem ipsum dolor</li>
      <li>○ Lorem ipsum dolor</li><li>○ Nemo enim ipsam</li>
    </ul>
    <span class="book centered">BOOK NOW</span>
  </div>
</section>

<h2 class="section-title abs" style="top:2533px">ABOUT BRIGHT HARBOR INSTITUTE</h2>
<svg class="divider abs" style="top:2586px" viewBox="0 0 290 48"><line x1="0" y1="24" x2="110" y2="24" stroke="#d9d9d9"/><line x1="180" y1="24" x2="290" y2="24" stroke="#d9d9d9"/><circle cx="145" cy="24" r="22" fill="#fff" stroke="#d9d9d9"/><circle cx="145" cy="24" r="8" fill="#2c5fa8"/></svg>

<section class="about-card abs">
  <h3>ABOUT US</h3>
  <p>Sed ut perspiciatis unde omnis iste natus error sit voluptatem accusantium doloremque laudantium, totam rem aperiam, eaque ipsa quae ab illo inventore veritatis et quasi architecto beatae vitae dicta sunt explicabo. Nemo enim ipsam voluptatem quia voluptas sit aspernatur aut odit aut fugit, sed quia consequuntur magni dolores eos qui ratione voluptatem sequi nesciunt. Neque porro quisquam est, qui dolorem ipsum quia dolor sit amet,Neque porro</p>
  <span class="about-btn centered">READ MORE</span>
</section>
<div class="about-photo abs" role="img" aria-label="Photo of a student resting her chin on her hands beside a laptop"></div>

<section class="contact abs">
  <h2>CONTACT US</h2>
</section>
<div class="field abs" style="left:112px;top:3265px;width:234px;height:41px">First Name</div>
<div class="field abs" style="left:352px;top:3265px;width:231px;height:41px">Last Name</div>
<div class="field abs" style="left:112px;top:3316px;width:234px;height:41px">Email</div>
<div class="field abs" style="left:352px;top:3316px;width:231px;height:41px">Phone</div>
<div class="field abs" style="left:112px;top:3369px;width:471px;height:158px">Message</div>
<div class="submit abs centered">SUBMIT</div>
<div class="map abs" role="img" aria-label="Street map showing the institute location"></div>

<footer class="site-footer abs">
  <div class="social abs" aria-label="Social links"><span></span><span></span><span></span><span></span></div>
  <div class="copyright abs">Copyrights © 2019 All Rights Reserved</div>
</footer>

</body>
</html>
```